MossVane Spa, Skincare and Cosmetics website

I need a website for MossVane (putting the glow back into people's skin) which allows viewers to access information about Beauty Spa packaging and facilities as well as online skincare and cosmetic products. Our distinctive difference is that our products are certified organic. We want to target a luxury high income niche market (age 30-50). I want all colours to be "baby colours" preferably background to be "baby metallic pink" (but please don't make the website too immature) with curves as patterns. I want a romantic vintage look.

The website needs to look:
1. elegant (prestige and luxury)
2. bright (baby colours mainly)
3. European curves and signature patterns
4. Can include Pearl related pics (but not a must)

The website pages needs to have:
1. pages ordering skincare/cosmetics
2. shopping cart and payment
3. about us and about our product differences
4. contact us
5. booking for spa treatments and packages

I have attached our logo and also packaging label styles.

Industry/Entity Type

Cosmetics

```html
<!DOCTYPE html>
<html lang="en">
<head>
<meta charset="utf-8">
<title>MossVane Spa, Skincare and Cosmetics</title>
<link rel="stylesheet" href="https://fonts.googleapis.com/css2?family=Cinzel:wght@400;600&family=Pacifico&family=Open+Sans:wght@400;600&display=swap">
<style>
  :root {
    --rose: #ea4d80;
    --rose-soft: #f4a3bb;
    --blush: #fbe4ee;
    --blush-deep: #f7cfe0;
    --frame-fill: #f5eaea;
    --frame-line: #d8b7b0;
    --taupe: #c6a59b;
    --leaf: #5cb548;
    --leaf-light: #7ccb6a;
    --leaf-dark: #3f8d31;
    --sky: #73a4da;
    --ink: #1f1f1f;
    --slate: #333333;
    --arrow: #9a9a9a;
  }
  * { box-sizing: border-box; margin: 0; padding: 0; }
  html, body { width: 1200px; height: 900px; overflow: hidden; }
  body {
    position: relative;
    font-family: "Open Sans", Arial, sans-serif;
    color: var(--ink);
    background: #ffffff;
  }
  .page-backdrop {
    position: absolute; inset: 0;
    background:
      radial-gradient(ellipse at 50% 50%, #fff6f9 0%, rgba(255,246,249,0) 60%),
      linear-gradient(180deg, var(--blush-deep) 0%, var(--blush) 35%, #fdf1f6 65%, var(--blush-deep) 100%);
  }
  .top-bar {
    position: absolute; left: 0; top: 0; width: 1200px; height: 42px;
    background: var(--rose);
  }
  .social-links { position: absolute; left: 225px; top: 8px; display: flex; gap: 12px; }
  .social-links span { width: 24px; height: 24px; border-radius: 50%; background: #ffffff; display: block; }
  .account-links {
    position: absolute; right: 220px; top: 8px; height: 26px;
    display: flex; align-items: center; gap: 6px; white-space: nowrap;
    font-family: "Cinzel", Georgia, serif; font-size: 12px; color: #ffffff;
  }
  .account-links .divider { opacity: .8; }
  .cart-link { display: flex; align-items: center; gap: 4px; font-family: "Pacifico", cursive; font-size: 20px; line-height: 1; }
  .frame-art { position: absolute; left: 0; top: 0; width: 1200px; height: 900px; }
  .brand {
    position: absolute; left: 402px; top: 96px; width: 420px; text-align: center;
  }
  .brand-dot { width: 52px; height: 52px; border-radius: 50%; background: #e0bfb3; margin: 0 auto 6px; }
  .brand-name { font-family: "Cinzel", Georgia, serif; font-size: 32px; color: var(--taupe); letter-spacing: 1px; line-height: 1; }
  .main-nav {
    position: absolute; left: 222px; top: 208px; width: 768px; height: 44px;
    display: flex; align-items: center; justify-content: space-between; padding-right: 14px;
  }
  .main-nav a {
    font-family: "Cinzel", Georgia, serif; font-size: 13px; color: #ffffff; text-decoration: none;
    white-space: nowrap; height: 44px; line-height: 44px; padding: 0 12px;
  }
  .main-nav a.is-active { background: var(--rose); }
  .hero {
    position: absolute; left: 234px; top: 252px; width: 736px; height: 205px; overflow: hidden;
    background:
      radial-gradient(ellipse 150px 190px at 150px 90px, #f1d2c2 0%, #f3ddd1 45%, rgba(250,243,239,0) 100%),
      radial-gradient(ellipse 200px 90px at 500px 120px, #ead2bb 0%, rgba(234,210,187,0) 100%),
      radial-gradient(ellipse 60px 80px at 610px 120px, #8a5a3c 0%, rgba(138,90,60,0) 100%),
      linear-gradient(90deg, #eee5e0 0%, #fbf8f6 45%, #ffffff 60%, #f8f5f1 100%);
  }
  .hero-arrow {
    position: absolute; top: 66px; width: 38px; height: 58px; background: var(--arrow);
    display: flex; align-items: center; justify-content: center;
  }
  .hero-arrow.prev { left: 0; }
  .hero-arrow.next { right: 0; }
  .welcome {
    position: absolute; left: 234px; top: 457px; width: 736px; height: 35px;
    text-align: center; font-family: "Cinzel", Georgia, serif; font-weight: 400; font-size: 22px; line-height: 35px; color: var(--taupe);
    background: #f3e7e6;
  }
  .feature-col { position: absolute; top: 502px; }
  .feature-col h2 { font-family: "Pacifico", cursive; font-weight: 400; font-size: 20px; line-height: 30px; white-space: nowrap; }
  .col-beliefs { left: 246px; width: 226px; }
  .col-beliefs h2 { color: var(--rose); }
  .col-beliefs p { font-size: 10px; line-height: 13px; margin-top: 6px; }
  .col-beliefs p + p { margin-top: 12px; }
  .col-featured { left: 486px; width: 232px; text-align: center; }
  .col-featured h2 { color: var(--leaf); }
  .col-visit { left: 725px; width: 230px; text-align: center; }
  .col-visit h2 { color: var(--sky); }
  .media-box {
    position: relative; margin-top: 2px; height: 125px; border: 1px solid #d5d5d5; overflow: hidden;
  }
  .product-shot {
    background:
      radial-gradient(ellipse 80px 45px at 100px 70px, #d9c9a8 0%, rgba(217,201,168,0) 100%),
      radial-gradient(ellipse 90px 30px at 110px 100px, #e6e6ea 0%, rgba(230,230,234,0) 100%),
      linear-gradient(180deg, #ffffff 0%, #f3f0ea 100%);
  }
  .new-flag {
    position: absolute; right: -22px; top: 12px; width: 90px; height: 20px; transform: rotate(45deg);
    background: #e78b9a; color: #ffffff; font-family: "Cinzel", Georgia, serif; font-size: 11px; line-height: 20px; text-align: center;
  }
  .map-area {
    background:
      radial-gradient(ellipse 40px 30px at 130px 75px, #f0d4cf 0%, rgba(240,212,207,0) 100%),
      linear-gradient(135deg, #efeadb 0%, #e9e5d8 50%, #f1eee4 100%);
  }
  .cta-row { position: absolute; top: 665px; left: 246px; width: 710px; height: 49px; }
  .cta {
    position: absolute; top: 0; height: 49px; color: #ffffff; text-decoration: none;
    font-family: "Pacifico", cursive; font-size: 23px; line-height: 49px; text-align: center; white-space: nowrap;
  }
  .cta-packages { left: 0; width: 232px; background: var(--rose-soft); }
  .cta-spa { left: 240px; width: 232px; background: var(--leaf); }
  .cta-sellers { left: 479px; width: 231px; background: var(--sky); }
  .frame-rule { position: absolute; left: 270px; top: 726px; width: 678px; border-top: 1px dashed var(--frame-line); }
  .frame-footer { position: absolute; left: 402px; top: 740px; width: 420px; text-align: center; }
  .frame-footer .name { font-family: "Cinzel", Georgia, serif; font-size: 24px; color: var(--taupe); line-height: 30px; }
  .frame-footer .phone { font-family: "Cinzel", Georgia, serif; font-size: 20px; color: var(--rose); line-height: 28px; }
  .site-footer {
    position: absolute; left: 0; top: 857px; width: 1200px; height: 43px; background: var(--slate);
    display: flex; align-items: center; justify-content: center; gap: 16px; white-space: nowrap;
    font-family: "Cinzel", Georgia, serif; font-size: 11px; color: #ffffff;
  }
  .site-footer nav { display: flex; gap: 5px; }
</style>
</head>
<body>
  <div class="page-backdrop" role="img" aria-label="Soft baby pink chevron background pattern"></div>

  <header class="top-bar">
    <div class="social-links">
      <span aria-label="Social page one"></span>
      <span aria-label="Social page two"></span>
    </div>
    <div class="account-links">
      <span>Login/Register</span><span class="divider">|</span>
      <span>View Order Status</span><span class="divider">|</span>
      <span class="cart-link">Cart
        <svg width="24" height="20" viewBox="0 0 24 20" aria-hidden="true">
          <path d="M1 2h4l3 11h12l3-8H7" fill="none" stroke="#fff" stroke-width="2.2" stroke-linejoin="round"/>
          <path d="M7 5h16l-3 8H9z" fill="#fff"/>
          <circle cx="10" cy="17" r="2" fill="#fff"/><circle cx="19" cy="17" r="2" fill="#fff"/>
        </svg>
      </span>
    </div>
  </header>

  <svg class="frame-art" viewBox="0 0 1200 900" aria-hidden="true">
    <path d="M238,146 H402 V92 A14 14 0 0 0 416,78 H808 A14 14 0 0 0 822,92 V146 H964 A14 14 0 0 0 978,160 V720 A14 14 0 0 0 964,734 H822 V814 A14 14 0 0 0 808,828 H416 A14 14 0 0 0 402,814 V734 H238 A14 14 0 0 0 224,720 V160 A14 14 0 0 0 238,146 Z"
      fill="var(--frame-fill)" stroke="var(--frame-line)" stroke-width="3"/>
    <path d="M244,153 H409 V97 A12 12 0 0 0 421,85 H803 A12 12 0 0 0 815,97 V153 H958 A12 12 0 0 0 970,165 V715 A12 12 0 0 0 958,727 H815 V809 A12 12 0 0 0 803,821 H421 A12 12 0 0 0 409,809 V727 H244 A12 12 0 0 0 232,715 V165 A12 12 0 0 0 244,153 Z"
      fill="none" stroke="#ffffff" stroke-width="1.5"/>
    <polygon points="162,214 222,214 222,258 162,258 178,236" fill="var(--leaf)"/>
    <polygon points="218,252 232,262 232,252" fill="var(--leaf-dark)"/>
    <polygon points="1042,214 982,214 982,258 1042,258 1026,236" fill="var(--leaf)"/>
    <polygon points="991,252 977,262 977,252" fill="var(--leaf-dark)"/>
    <rect x="218" y="208" width="773" height="44" fill="var(--leaf)"/>
    <rect x="218" y="208" width="773" height="3" fill="var(--leaf-light)"/>
  </svg>

  <div class="brand">
    <div class="brand-dot"></div>
    <div class="brand-name">MossVane</div>
  </div>

  <nav class="main-nav">
    <a class="is-active" href="#">Home</a>
    <a href="#">Makeup</a>
    <a href="#">Skincare</a>
    <a href="#">Gifts</a>
    <a href="#">Beauty Tips</a>
    <a href="#">About Us</a>
    <a href="#">Clearance</a>
    <a href="#">Offers</a>
    <a href="#">Contact Us</a>
  </nav>

  <section class="hero" role="img" aria-label="Slide: woman with glowing skin beside organic skincare jars, boxes and amber dropper bottles">
    <span class="hero-arrow prev"><svg width="16" height="26" viewBox="0 0 16 26" aria-hidden="true"><path d="M13 2 3 13l10 11" fill="none" stroke="#fff" stroke-width="2"/></svg></span>
    <span class="hero-arrow next"><svg width="16" height="26" viewBox="0 0 16 26" aria-hidden="true"><path d="M3 2l10 11L3 24" fill="none" stroke="#fff" stroke-width="2"/></svg></span>
  </section>

  <h1 class="welcome">Welcome to MossVane</h1>

  <section class="feature-col col-beliefs">
    <h2>What we believe in</h2>
    <p>This particular section is to demonstrate what the welcome paragraph can look like. You can replace information in this area with anything you like, including, but not limited to, a mission statement or maybe even an “about us” section.</p>
    <p>This could be setup for a secondary paragraph if you have more than one paragraph worth of information.</p>
  </section>

  <section class="feature-col col-featured">
    <h2>Featured Product</h2>
    <div class="media-box product-shot" role="img" aria-label="Featured organic skincare product range of bottles and boxes">
      <span class="new-flag">New!</span>
    </div>
  </section>

  <section class="feature-col col-visit">
    <h2>Come Visit Us!</h2>
    <div class="media-box map-area" role="img" aria-label="Street map showing the spa location"></div>
  </section>

  <div class="cta-row">
    <a class="cta cta-packages" href="#">Our Packages</a>
    <a class="cta cta-spa" href="#">Spa Treatments</a>
    <a class="cta cta-sellers" href="#">Top Sellers</a>
  </div>

  <div class="frame-rule"></div>
  <div class="frame-footer">
    <div class="name">MossVane</div>
    <div class="phone">1-800-000-0000</div>
  </div>

  <footer class="site-footer">
    <span>Copyright © 2014 MossVane. All rights reserved.</span>
    <nav>
      <span>Privacy Policy</span><span>|</span>
      <span>Terms &amp; Conditions</span><span>|</span>
      <span>About Us</span><span>|</span>
      <span>FAQ</span><span>|</span>
      <span>Sitemap</span>
    </nav>
  </footer>
</body>
</html>
```